Consulting firm needs a professional letterhead design

We need a professional letterhead design which is simple but unique. It should carry attributes of the latest designs in the market suitable for professional environmental consultancies.

- The logo is attached for you to USE.
- Our preferred color scheme is that shown in the logo.
- Letterhead text color is your choice to make.
- Logo to the left and text to the right plus slogan/tagline is desirable for this letterhead.

Use any address etc. of your choice in the letterhead.

Target Market(s)

Consulting firms and government agencies

Industry/Entity Type

Environmental Consultant

Colors
acd037
fece3e
85cae6
3277b5

Requirements
Must have
• Logo supplied and color scheme must be used.
Nice to have
• Nexa font is used in the Logo, so it would ne nice to have nexa font in the letterhead too.

```html
<!DOCTYPE html>
<html lang="en">
<head>
<meta charset="utf-8">
<title>Verdalis Letterhead</title>
<link href="https://fonts.googleapis.com/css2?family=Didact+Gothic&family=Montserrat:wght@600;700&display=swap" rel="stylesheet">
<style>
  :root {
    --blue: #3277b5;
    --green: #acd037;
    --navy: #2b3150;
    --ink: #2a2a2a;
    --paper: #ffffff;
    --backdrop: #ffffff;
  }
  * { margin: 0; padding: 0; box-sizing: border-box; }
  html, body { width: 881px; height: 1200px; overflow: hidden; background: var(--backdrop); }
  .canvas { position: relative; width: 881px; height: 1200px; }
  .sheet {
    position: absolute; left: 67px; top: 70px; width: 747px; height: 1058px;
    background: var(--paper);
    box-shadow: 0 0 6px rgba(0,0,0,0.35);
    overflow: hidden;
  }
  .abs { position: absolute; }
  .header-band {
    left: 0; top: 0; width: 747px; height: 138px;
    background: linear-gradient(100deg, var(--blue) 0%, var(--blue) 55%, var(--green) 100%);
  }
  .footer-band {
    left: 0; bottom: 0; width: 747px; height: 75px;
    background: linear-gradient(100deg, var(--green) 0%, var(--blue) 45%, var(--blue) 100%);
  }
  .brand { left: 41px; top: 172px; display: flex; align-items: center; gap: 12px; }
  .brand-mark { width: 52px; height: 52px; background: var(--green); }
  .brand-name {
    font-family: "Montserrat", sans-serif; font-weight: 700; font-size: 29px;
    letter-spacing: 1px; color: var(--navy);
  }
  .header-rule { left: 381px; top: 206px; width: 328px; height: 3px; background: var(--navy); }
  .sender-name {
    font-family: "Montserrat", sans-serif; font-weight: 700; font-size: 16px;
    color: var(--navy); line-height: 1;
  }
  .sender-role {
    font-family: "Montserrat", sans-serif; font-weight: 600; font-size: 8.5px;
    color: var(--ink); margin-top: 3px;
  }
  .sender-top { left: 108px; top: 355px; }
  .sender-bottom { left: 108px; top: 955px; }
  .letter-date {
    right: 105px; top: 361px;
    font-family: "Montserrat", sans-serif; font-weight: 700; font-size: 11px; color: var(--navy);
  }
  .letter-date .label { font-weight: 600; }
  .body-para {
    left: 108px; white-space: nowrap;
    font-family: "Didact Gothic", sans-serif; font-size: 12.4px; letter-spacing: 0.2px;
    line-height: 15.3px; color: var(--ink);
  }
  .signature {
    left: 110px; top: 876px; width: 177px; height: 42px;
    background: linear-gradient(90deg, rgba(30,30,30,0.18), rgba(30,30,30,0.05));
    border-radius: 20px;
  }
  .contact-list { right: 96px; top: 865px; list-style: none; }
  .contact-item {
    display: flex; align-items: center; justify-content: flex-end; gap: 10px;
    height: 25px; margin-bottom: 7.6px;
    font-family: "Didact Gothic", sans-serif; font-size: 15px; color: var(--ink);
  }
  .contact-icon {
    width: 25px; height: 25px; background: var(--blue);
    display: flex; align-items: center; justify-content: center;
  }
  .contact-icon svg { width: 14px; height: 14px; }
</style>
</head>
<body>
<div class="canvas">
  <div class="sheet">
    <div class="abs header-band" role="img" aria-label="Decorative header band in blue and green"></div>
    <div class="abs footer-band" role="img" aria-label="Decorative footer band in green and blue"></div>

    <div class="abs brand">
      <span class="brand-mark"></span>
      <span class="brand-name">VERDALIS</span>
    </div>
    <div class="abs header-rule"></div>
  </div>

  <div class="abs sender-top">
    <div class="sender-name">MARTIN HALE</div>
    <div class="sender-role">FOUNDER &amp; CEO</div>
  </div>
  <div class="abs letter-date"><span class="label">DATE :</span> 22 - JUNE - 2020</div>

  <p class="abs body-para" style="top:432px;">Lorem ipsum dolor sit amet, consectetuer adipiscing elit, sed diam nonummy nibh euismod tincidunt ut laoreet<br>dolore magna aliquam erat volutpat. Ut wisi enim ad minim veniam, quis nostrud exerci tation ullamcorper<br>suscipit lobortis nisl ut aliquip ex ea commodo consequat. Duis autem vel eum iriure dolor in hendrerit in vulpu-<br>tate velit esse molestie consequat, vel illum dolore eu feugiat nulla facilisis at vero eros et accumsan et iusto odio<br>dignissim qui blandit praesent luptatum zzril delenit augue duis dolore te feugait nulla facilisi.</p>
  <p class="abs body-para" style="top:539px;">Lorem ipsum dolor sit amet, cons ectetuer adipiscing elit, sed diam nonummy nibh euismod tincidunt ut laoreet<br>dolore magna aliquam erat volutpat. Ut wisi enim ad minim veniam, quis nostrud exerci tation ullamcorper<br>suscipit lobortis nisl ut aliquip ex ea commodo consequat.</p>
  <p class="abs body-para" style="top:615px;">Lorem ipsum dolor sit amet, consectetuer adipiscing elit, sed diam nonummy nibh euismod tincidunt ut laoreet<br>dolore magna aliquam erat volutpat. Ut wisi enim ad minim veniam, quis nostrud exerci tation ullamcorper<br>suscipit lobortis nisl ut aliquip ex ea commodo consequat. Duis autem vel eum iriure dolor in hendrerit in vulpu-<br>tate velit esse molestie consequat, vel illum dolore eu feugiat nulla facilisis at vero eros et accumsan et iusto odio<br>dignissim qui blandit praesent luptatum zzril delenit augue duis dolore te feugait nulla facilisi.</p>
  <p class="abs body-para" style="top:722px;">Lorem ipsum dolor sit amet, cons ectetuer adipiscing elit, sed diam nonummy nibh euismod tincidunt ut laoreet<br>dolore magna aliquam erat volutpat. Ut wisi enim ad minim veniam, quis nostrud exerci tation ullamcorper<br>suscipit lobortis nisl ut aliquip ex ea commodo consequat.</p>
  <p class="abs body-para" style="top:783px;">Lorem ipsum dolor sit amet, consectetuer adipiscing elit, sed diam nonummy nibh euismod tincidunt ut laoreet<br>dolore magna aliquam erat volutpat. Ut wisi enim ad minim veniam, quis nostrud exerci tation</p>

  <div class="abs signature" role="img" aria-label="Handwritten signature of the sender"></div>
  <div class="abs sender-bottom">
    <div class="sender-name">MARTIN HALE</div>
    <div class="sender-role">FOUNDER &amp; CEO</div>
  </div>

  <ul class="abs contact-list">
    <li class="contact-item">(03) 5120 4410
      <span class="contact-icon"><svg viewBox="0 0 24 24"><path fill="#fff" d="M6.6 10.8a15 15 0 0 0 6.6 6.6l2.2-2.2a1 1 0 0 1 1-.25 11.4 11.4 0 0 0 3.6.57 1 1 0 0 1 1 1V20a1 1 0 0 1-1 1A17 17 0 0 1 3 4a1 1 0 0 1 1-1h3.5a1 1 0 0 1 1 1c0 1.25.2 2.45.57 3.57a1 1 0 0 1-.25 1z"/></svg></span></li>
    <li class="contact-item">(03) 5120 4411
      <span class="contact-icon"><svg viewBox="0 0 24 24"><path fill="#fff" d="M7 3h10v5H7zM4 9h16a2 2 0 0 1 2 2v6h-4v4H6v-4H2v-6a2 2 0 0 1 2-2zm4 7v3h8v-3z"/></svg></span></li>
    <li class="contact-item">office@verdalis.com
      <span class="contact-icon"><svg viewBox="0 0 24 24"><path fill="#fff" d="M2 5h20v14H2zm2 2v.5l8 5.5 8-5.5V7zm0 3v7h16v-7l-8 5.5z"/></svg></span></li>
    <li class="contact-item">www.verdalis.com
      <span class="contact-icon"><svg viewBox="0 0 24 24"><circle cx="12" cy="12" r="9" fill="none" stroke="#fff" stroke-width="2"/><path d="M3 12h18M12 3c3 3 3 15 0 18M12 3c-3 3-3 15 0 18" fill="none" stroke="#fff" stroke-width="1.6"/></svg></span></li>
    <li class="contact-item">PO Box 418, Ashvale, Vic, 3520
      <span class="contact-icon"><svg viewBox="0 0 24 24"><path fill="#fff" d="M12 2a7 7 0 0 1 7 7c0 5-7 13-7 13S5 14 5 9a7 7 0 0 1 7-7zm0 4a3 3 0 1 0 0 6 3 3 0 0 0 0-6z"/></svg></span></li>
  </ul>
</div>
</body>
</html>
```